VelorDrive/Pindux: map and navigation, GIS, ICT, B2B, technology, IT projects

Company profile: Tech company, national leader (Poland) in mapping and car nav solutions. The main brand is VelorDrive for which we recently had a logo lift. Pindux is the brand of business GIS products and we present it as "Pindux by VelorDrive".

Attachements:
- VelorDrive logo,
- VelorDrive application icon,
- Pindux by VelorDrive logo,
- VelorDrive LogoGuide with approved colors,
- few sample slides,
- link to Polish regions: https://shrt.example/qK7wR2
- link to our www: velordrive.pl & pindux.pl

Target Market(s)

We focus on the domestic market. Our main B2B customers are international companies operating on the Polish market.

Font styles to use
Serif
Sans Serif
Other font styles liked:
• Lato, Artegra_Sans

Colors
0455a3
3176b5
85abd2
9bcb3b

Requirements
Must have
• Expectations: consistency of graphic layout of all presentation templates (business, portfolio, advertising, etc.). The color scheme should be consistent with our brands. We expect colors, style, fonts, layouts and a set of icons in the project. For stock photos please use stockvelt.com.
• Expected stylistics: elegant, technological, business, modern. Please note that the proposed fonts should contain polish characters (ą ę ł ś ć ż ź ó).
• We expect a dozen or so templates of slides. Among them should be:
• - Title + midpage title,
• - Table of contents / agenda,
• - Slide: 2-3 graphics + text,
• - Slide: only graphics (4-8),
• - Slide: typical for the portfolio (clients' logos, graphics, text),
• - Slide: timeline + project milestones overview,
• - Slide with the offer and prices with description
• - (!) Some creative ideas for infographics related to maps,
• - Couple of structure and proccess SmartArt,
• - "Contact us" slide

```html
<!DOCTYPE html>
<html lang="en">
<head>
<meta charset="utf-8">
<title>VelorDrive presentation templates</title>
<link href="https://fonts.googleapis.com/css2?family=Open+Sans:wght@400;600;700&display=swap" rel="stylesheet">
<style>
  :root {
    --canvas: #000000;
    --paper: #ffffff;
    --brand-navy: #2b50a0;
    --brand-sky: #7fa3d8;
    --brand-green: #8fd14f;
    --hero-top: #2d72f2;
    --hero-bottom: #0a2fbf;
    --body-grey: #8a8a8a;
    --rule-grey: #c9c9c9;
    --footer-band: #efefef;
    --footer-text: #444444;
  }
  * { box-sizing: border-box; margin: 0; padding: 0; }
  html, body { width: 1200px; height: 680px; overflow: hidden; background: var(--canvas); }
  body { position: relative; font-family: "Open Sans", Arial, sans-serif; }

  .slide { position: absolute; background: var(--paper); overflow: hidden; }
  .slide--title   { left: 30px;  top: 24px;  width: 555px; height: 310px; }
  .slide--bullets { left: 616px; top: 32px;  width: 556px; height: 302px; }
  .slide--feature { left: 31px;  top: 350px; width: 556px; height: 302px; }
  .slide--columns { left: 616px; top: 350px; width: 556px; height: 302px; }

  /* title slide */
  .hero-shape { position: absolute; inset: 0; width: 100%; height: 100%; }
  .hero-rule { position: absolute; left: 53px; top: 190px; width: 1px; height: 120px; background: rgba(255,255,255,.55); }
  .hero-accent { position: absolute; left: 50px; top: 218px; width: 4px; height: 40px; background: var(--brand-green); border-radius: 2px; }
  .hero-title { position: absolute; left: 66px; top: 220px; color: #fff; font-weight: 700; font-size: 22px; line-height: 1.2; }
  .hero-subtitle { position: absolute; left: 66px; top: 248px; color: #fff; font-size: 17px; line-height: 1.2; }
  .hero-wordmark { position: absolute; left: 353px; top: 120px; color: var(--brand-navy); font-weight: 600; font-size: 34px; letter-spacing: -0.5px; }

  /* shared content-slide parts */
  .wordmark { position: absolute; right: 15px; top: 10px; color: var(--brand-navy); font-weight: 600; font-size: 19px; letter-spacing: -0.3px; }
  .side-rule { position: absolute; left: 28px; top: 0; width: 1px; background: var(--rule-grey); }
  .heading-accent { position: absolute; width: 4px; height: 40px; background: var(--brand-green); border-radius: 2px; }
  .heading { position: absolute; }
  .heading__kicker { color: var(--brand-sky); font-size: 14px; line-height: 17px; }
  .heading__title { color: var(--brand-navy); font-weight: 700; font-size: 17.5px; line-height: 21px; }
  .body-copy { color: var(--body-grey); font-size: 8.6px; line-height: 14.4px; }

  .footer { position: absolute; left: 0; right: 0; bottom: 0; height: 16px; background: var(--footer-band); }
  .footer__copy { position: absolute; left: 9px; top: 3px; font-size: 8.6px; color: var(--footer-text); }
  .page-badge { position: absolute; right: 5px; bottom: 2px; width: 20px; height: 20px; border-radius: 50%; background: var(--brand-navy); color: #fff; font-size: 8px; font-weight: 700; display: flex; align-items: center; justify-content: center; }

  /* bullet slide */
  .bullet-list { position: absolute; left: 36px; top: 86px; width: 500px; list-style: none; }
  .bullet { position: relative; padding-left: 27px; margin-bottom: 14px; }
  .bullet__dot { position: absolute; left: 4px; top: 5px; width: 10px; height: 10px; border-radius: 50%; background: var(--brand-navy); }
  .bullet__title { color: var(--brand-green); font-weight: 700; font-size: 12px; line-height: 16px; }
  .bullet .body-copy { font-size: 8.4px; line-height: 13px; width: 445px; }

  /* feature slide */
  .feature-copy { position: absolute; left: 258px; top: 125px; width: 268px; }

  /* two-column slide */
  .columns { position: absolute; left: 42px; top: 74px; width: 494px; display: flex; gap: 28px; }
  .columns .body-copy { flex: 1; }
</style>
</head>
<body>

  <section class="slide slide--title">
    <svg class="hero-shape" viewBox="0 0 555 310" preserveAspectRatio="none" aria-hidden="true">
      <defs>
        <linearGradient id="heroGradient" x1="0" y1="0" x2="0" y2="1">
          <stop offset="0" stop-color="var(--hero-top)"/>
          <stop offset="1" stop-color="var(--hero-bottom)"/>
        </linearGradient>
      </defs>
      <polygon points="0,0 222,0 427,310 0,310" fill="url(#heroGradient)"/>
      <polygon points="468,0 555,0 555,114" fill="var(--brand-green)"/>
    </svg>
    <div class="hero-rule"></div>
    <div class="hero-accent"></div>
    <h1 class="hero-title">Project Title Here</h1>
    <p class="hero-subtitle">Subtitle Here</p>
    <div class="hero-wordmark">VelorDrive</div>
  </section>

  <section class="slide slide--bullets">
    <div class="side-rule" style="height:110px"></div>
    <div class="heading-accent" style="left:26px; top:30px"></div>
    <div class="heading" style="left:42px; top:33px">
      <p class="heading__kicker">Subtitle Here</p>
      <h2 class="heading__title">Bullet Slides</h2>
    </div>
    <div class="wordmark">VelorDrive</div>
    <ul class="bullet-list">
      <li class="bullet"><span class="bullet__dot"></span>
        <p class="bullet__title">Bullet text Here</p>
        <p class="body-copy">Lorem Ipsum is simply dummy text of the printing and typesetting industry. Lorem Ipsum has been the industry's standard dummy text ever since the 1500s, when an unknown printer took a galley of type and scrambled it to make a type specimen book.</p>
      </li>
      <li class="bullet"><span class="bullet__dot"></span>
        <p class="bullet__title">Bullet text Here</p>
        <p class="body-copy">Lorem Ipsum is simply dummy text of the printing and typesetting industry. Lorem Ipsum has been the industry's standard dummy text ever since the 1500s, when an unknown printer took a galley of type and scrambled it to make a type specimen book.</p>
      </li>
      <li class="bullet"><span class="bullet__dot"></span>
        <p class="bullet__title">Bullet text Here</p>
        <p class="body-copy">Lorem Ipsum is simply dummy text of the printing and typesetting industry. Lorem Ipsum has been the industry's standard dummy text ever since the 1500s, when an unknown printer took a galley of type and scrambled it to make a type specimen book.</p>
      </li>
    </ul>
    <footer class="footer"><span class="footer__copy">Copyright text here</span></footer>
    <div class="page-badge">01</div>
  </section>

  <section class="slide slide--feature">
    <div class="side-rule" style="left:245px; height:266px"></div>
    <div class="heading-accent" style="left:243px; top:79px"></div>
    <div class="heading" style="left:258px; top:82px">
      <p class="heading__kicker">Subtitle Here</p>
      <h2 class="heading__title">Paragraph Title</h2>
    </div>
    <div class="wordmark">VelorDrive</div>
    <p class="body-copy feature-copy">Lorem Ipsum is simply dummy text of the printing and typesetting industry. Lorem Ipsum has been the industry's standard dummy text ever since the 1500s, when an unknown printer took a galley of type and scrambled it to make a type specimen book. It has survived not only five centuries, but also the leap into electronic typesetting, remaining essentially unchanged. It was popularised in the 1960s with the release of Glyphset sheets containing Lorem Ipsum passages, and more recently with desktop publishing software like Pressmill Layout including versions of Lorem Ipsum.</p>
    <footer class="footer"><span class="footer__copy">Copyright text here</span></footer>
    <div class="page-badge">01</div>
  </section>

  <section class="slide slide--columns">
    <div class="side-rule" style="height:104px"></div>
    <div class="heading-accent" style="left:26px; top:31px"></div>
    <div class="heading" style="left:42px; top:31px">
      <p class="heading__kicker">Subtitle Here</p>
      <h2 class="heading__title">Paragraph Title</h2>
    </div>
    <div class="wordmark">VelorDrive</div>
    <div class="columns">
      <p class="body-copy">Lorem Ipsum is simply dummy text of the printing and typesetting industry. Lorem Ipsum has been the industry's standard dummy text ever since the 1500s, when an unknown printer took a galley of type and scrambled it to make a type specimen book. It has survived not only five centuries, but also the leap into electronic typesetting, remaining essentially unchanged. It was popularised in the 1960s with the release of Glyphset sheets containing Lorem Ipsum passages, and more recently with desktop publishing software like Pressmill Layout including versions of Lorem Ipsum. Lorem Ipsum is simply dummy text of the printing and typesetting industry. Lorem Ipsum has been the industry's</p>
      <p class="body-copy">Lorem Ipsum is simply dummy text of the printing and typesetting industry. Lorem Ipsum has been the industry's standard dummy text ever since the 1500s, when an unknown printer took a galley of type and scrambled it to make a type specimen book. It has survived not only five centuries, but also the leap into electronic typesetting, remaining essentially unchanged. It was popularised in the 1960s with the release of Glyphset sheets containing Lorem Ipsum passages, and more recently with desktop publishing software like Pressmill Layout including versions of Lorem Ipsum. Lorem Ipsum is simply dummy text of the printing and typesetting industry. Lorem Ipsum has been the industry's</p>
    </div>
    <footer class="footer"><span class="footer__copy">Copyright text here</span></footer>
    <div class="page-badge">01</div>
  </section>

</body>
</html>
```